Business card for Internet Marketing Consultant

Simple - need a nice business card design using the logo elements and colors. Keywords: Progressive, professional, stylish, minimalist. Please use the kr as part of the design.

Info for card:

Gareth Pennock
Internet Marketing Strategist
Phone: (555) 813-2064
Email: gareth@korvantareach.com
Address: 2156 N. Halvern Ave., Ste. 118
Brenmoor, Arizona 85963

Website: www.korvantareach.com

Business

Sans Serif

```html
<!DOCTYPE html>
<html lang="en">
<head>
<meta charset="utf-8">
<title>Korvanta Reach – Business Card</title>
<link href="https://fonts.googleapis.com/css2?family=Lato:wght@400;700;900&display=swap" rel="stylesheet">
<style>
  :root{
    --bg:#2b2b2b;
    --card:#f7f7f7;
    --brand-blue:#1565c0;
    --brand-green:#5aa55e;
    --ink:#1c1c1c;
    --muted:#8a8a8a;
    --rule:#111111;
  }
  *{margin:0;padding:0;box-sizing:border-box}
  html,body{width:1200px;height:997px;overflow:hidden}
  body{background:var(--bg);position:relative;font-family:"Lato",sans-serif}
  .card{
    position:absolute;width:600px;height:343px;background:var(--card);
    overflow:hidden;box-shadow:0 18px 40px rgba(0,0,0,.45);
  }
  .card--front{left:80px;top:70px}
  .card--back{left:520px;top:560px}
  .card__bands{position:absolute;left:0;bottom:0;width:600px;height:70px}

  .wordmark{display:flex;align-items:center;gap:10px}
  .wordmark__dot{width:18px;height:18px;border-radius:50%;background:var(--brand-green);flex:none}
  .wordmark__name{color:var(--brand-blue);font-weight:700;letter-spacing:.2px;white-space:nowrap}
  .tagline{color:var(--muted);text-transform:uppercase;margin-top:2px;white-space:nowrap}

  .front__brand{position:absolute;left:70px;top:110px}
  .front__brand .wordmark__name{font-size:46px}
  .front__brand .tagline{font-size:14px;letter-spacing:4.2px;margin-left:28px}
  .front__web{position:absolute;left:260px;top:230px;color:var(--muted);font-size:15px;letter-spacing:2px}

  .back__brand{position:absolute;left:40px;top:140px}
  .back__brand .wordmark__name{font-size:30px}
  .back__brand .wordmark__dot{width:14px;height:14px}
  .back__brand .tagline{font-size:9px;letter-spacing:2.4px;margin-left:24px}
  .back__divider{position:absolute;left:312px;top:60px;width:3px;height:190px;background:var(--rule)}
  .person{position:absolute;left:345px;top:52px;text-align:center;width:220px}
  .person__name{color:var(--brand-blue);font-weight:900;font-size:18px}
  .person__title{color:var(--ink);font-weight:700;font-size:10px;text-transform:uppercase;margin-top:2px}
  .contacts{position:absolute;left:340px;top:140px;list-style:none}
  .contacts li{display:flex;align-items:flex-start;gap:10px;color:var(--ink);font-weight:700;font-size:13px;line-height:17px;margin-bottom:5px;white-space:nowrap}
  .contacts svg{width:14px;height:14px;flex:none;margin-top:2px;fill:var(--brand-blue)}
</style>
</head>
<body>

<section class="card card--front" aria-label="Card front">
  <div class="front__brand">
    <div class="wordmark"><span class="wordmark__dot"></span><span class="wordmark__name">korvantareach</span></div>
    <div class="tagline">Internet Marketing Strategies</div>
  </div>
  <div class="front__web">www.korvantareach.com</div>
  <svg class="card__bands" viewBox="0 0 600 70" preserveAspectRatio="none" aria-hidden="true">
    <path d="M405 48 Q410 26 440 24 L600 12 L600 52 Z" fill="var(--brand-green)"/>
    <path d="M0 62 L600 48 L600 58 L0 70 Z" fill="var(--brand-blue)"/>
  </svg>
</section>

<section class="card card--back" aria-label="Card back">
  <div class="back__brand">
    <div class="wordmark"><span class="wordmark__dot"></span><span class="wordmark__name">korvantareach</span></div>
    <div class="tagline">Internet Marketing Strategies</div>
  </div>
  <div class="back__divider"></div>
  <div class="person">
    <div class="person__name">Gareth Pennock</div>
    <div class="person__title">Internet Marketing Strategist</div>
  </div>
  <ul class="contacts">
    <li><svg viewBox="0 0 24 24"><path d="M6.6 10.8a15 15 0 0 0 6.6 6.6l2.2-2.2a1 1 0 0 1 1-.25 11.4 11.4 0 0 0 3.6.57 1 1 0 0 1 1 1V20a1 1 0 0 1-1 1A17 17 0 0 1 3 4a1 1 0 0 1 1-1h3.5a1 1 0 0 1 1 1c0 1.25.2 2.45.57 3.57a1 1 0 0 1-.25 1z"/></svg>(555) 813-2064</li>
    <li><svg viewBox="0 0 24 24"><path d="M2 5h20v14H2z"/><path d="M3 6l9 7 9-7" stroke="#fff" stroke-width="1.6" fill="none"/></svg>gareth@korvantareach.com</li>
    <li><svg viewBox="0 0 24 24"><path d="M12 3 2 12h3v9h5v-6h4v6h5v-9h3z"/></svg>2156 N. Halvern Ave., Ste. 118<br>Brenmoor, Arizona 85963</li>
  </ul>
  <svg class="card__bands" viewBox="0 0 600 70" preserveAspectRatio="none" aria-hidden="true">
    <path d="M405 48 Q410 26 440 24 L600 12 L600 52 Z" fill="var(--brand-green)"/>
    <path d="M0 62 L600 48 L600 58 L0 70 Z" fill="var(--brand-blue)"/>
  </svg>
</section>

</body>
</html>
```